Quarterly Growth Letter needs a Letterhead

Our firm, BRV Solutions produces "Tobias's Quarterly Growth Letter", a monthly digest of marketing tips and tips for business owners in the MENA region. We use Postlyne to distribute this memo to our database each month. We are looking for a designer to put together a letterhead for this memo.

The goal of the memo is to produce original, relevant, and new content to readers. We are a quickly adapting company. We provide fresh material, and the branding and logo of the newsletter heading should reflect this.

What the letterhead should include:
- Our BRV Solutions logo (provided by me)
- The words "Tobias's Quarterly Growth Letter"
- Tobias's picture (provided by me)

It should be in a jpg or png format so that I can load it into the Postlyne template. The template is designed to be a traditional A4 in width.

To receive our logo and Tobias's picture for your design, please email me at jordan@brvsolutions.example.

Target Market(s)

Companies in the MENA region that are looking to dramatically improve their sales and marketing.

Industry/Entity Type

Marketing

Requirements
Must have
• The letterhead must be neat and have a clean design.
Should not have
• Too many colors, swirls or soft fonts.

```html
<!DOCTYPE html>
<html lang="en">
<head>
<meta charset="utf-8">
<title>BRV Solutions – Quarterly Growth Letter Letterhead</title>
<link href="https://fonts.googleapis.com/css2?family=Open+Sans:wght@400;600;700&display=swap" rel="stylesheet">
<style>
  :root {
    --brand-blue: #29abe2;
    --brand-gray: #939598;
    --text-gray: #8c8e91;
    --sheet: #ffffff;
    --backdrop-light: #bdbdbd;
    --backdrop-dark: #969696;
    --photo-warm: #d9b99a;
    --photo-dark: #3a3536;
  }
  * { box-sizing: border-box; margin: 0; padding: 0; }
  html, body { width: 1200px; height: 900px; overflow: hidden; }
  body {
    position: relative;
    font-family: "Open Sans", Arial, sans-serif;
    background: radial-gradient(ellipse at 45% 35%, var(--backdrop-light), var(--backdrop-dark));
  }
  .sheet {
    position: absolute;
    top: 89px;
    width: 510px;
    height: 721px;
    background: var(--sheet);
    box-shadow: 11px 12px 6px rgba(0,0,0,0.45);
    overflow: hidden;
  }
  .sheet--logo-top { left: 68px; }
  .sheet--logo-bottom { left: 623px; }
  .corner-art { position: absolute; inset: 0; width: 510px; height: 721px; }
  .brand {
    position: absolute;
    display: flex;
    align-items: center;
    gap: 12px;
  }
  .brand__dot {
    width: 34px; height: 34px;
    border-radius: 50%;
    background: var(--brand-blue);
    flex: none;
  }
  .brand__name {
    font-weight: 600;
    font-size: 28px;
    line-height: 34px;
    color: var(--text-gray);
    white-space: nowrap;
  }
  .sheet--logo-top .brand { left: 140px; top: 38px; }
  .sheet--logo-bottom .brand { left: 18px; top: 656px; }
  .memo-title {
    position: absolute;
    font-weight: 700;
    font-size: 16px;
    letter-spacing: 0.6px;
    color: var(--text-gray);
    white-space: nowrap;
  }
  .memo-title__name { color: var(--brand-blue); }
  .sheet--logo-top .memo-title { left: 0; right: 0; text-align: center; top: 91px; }
  .sheet--logo-bottom .memo-title { left: 72px; top: 32px; }
  .portrait {
    position: absolute;
    background: linear-gradient(180deg, var(--photo-warm) 0%, var(--photo-warm) 55%, var(--photo-dark) 75%, var(--photo-dark) 100%);
  }
  .sheet--logo-top .portrait { left: 407px; top: 593px; width: 93px; height: 121px; }
  .sheet--logo-bottom .portrait { left: 434px; top: 628px; width: 68px; height: 88px; }
</style>
</head>
<body>

  <section class="sheet sheet--logo-top">
    <div class="portrait" role="img" aria-label="Portrait photo of Tobias"></div>
    <svg class="corner-art" viewBox="0 0 510 721" aria-hidden="true">
      <polygon points="0,0 89,0 0,89" fill="var(--brand-blue)"/>
      <rect x="25" y="26" width="90" height="90" fill="var(--sheet)"/>
      <polygon points="510,634 510,721 422,721" fill="var(--brand-gray)"/>
    </svg>
    <div class="brand">
      <span class="brand__dot"></span>
      <span class="brand__name">BRV Solutions</span>
    </div>
    <h1 class="memo-title"><span class="memo-title__name">TOBIAS'S</span> QUARTERLY GROWTH LETTER</h1>
  </section>

  <section class="sheet sheet--logo-bottom">
    <svg class="corner-art" viewBox="0 0 510 721" aria-hidden="true">
      <polygon points="0,0 89,0 0,89" fill="var(--brand-blue)"/>
      <rect x="25" y="26" width="90" height="90" fill="var(--sheet)"/>
      <polygon points="510,0 510,89 422,89" fill="var(--brand-gray)"/>
    </svg>
    <h1 class="memo-title"><span class="memo-title__name">TOBIAS'S</span> QUARTERLY GROWTH LETTER</h1>
    <div class="portrait" role="img" aria-label="Portrait photo of Tobias"></div>
    <div class="brand">
      <span class="brand__dot"></span>
      <span class="brand__name">BRV Solutions</span>
    </div>
  </section>

</body>
</html>
```